Walking Beside the Quiet River; A Study of Refuge, Purpose & Calling

I need a book cover, for the above book title. This is a journey of the heart to know the heart of God. I think on the text, Simple (see below graphic)
Black Lettering for Knowing.....Intimately
Gold lettering for God
Either gold or black for the subtitle; A Study of Refuge, Purpose, & Calling
I would like the below graphic idea only no photograph of a person,
and White background instead of black
Simple Font, like below graphic, but open to suggestions

Target Market(s)

not age specific, Every person has been given a heart to know God, we are taking the mystery out the process to understand God is Father, loving gracious, ever present, etc. If we know His heart, we realize He's not at a distance, He is there, an ever present help

Industry/Entity Type

Security

Requirements
Must have
• Title: Walking Beside the Quiet River; A Study of Refuge, Purpose, & Calling
• My name, Tom Pettigrew
Nice to have
• See Below Graphic

```html
<!DOCTYPE html>
<html lang="en">
<head>
<meta charset="UTF-8">
<title>Walking Beside the Quiet River – Cover Wrap</title>
<link href="https://fonts.googleapis.com/css2?family=Montserrat:wght@600;700;800&family=Open+Sans:wght@400;600&display=swap" rel="stylesheet">
<style>
  :root {
    --page-bg: #e8e2d8;
    --paper: #ffffff;
    --ink: #111111;
    --ink-body: #3a3a3a;
    --gold: #c8942a;
    --glow: #ffe39a;
    --sunset: #eda24a;
    --dusk: #d9a98a;
    --field: #8a6a45;
    --road: #4a4048;
    --road-deep: #2e2a32;
    --portrait: #b7b9be;
    --edge: #d8d4cc;
  }
  html, body {
    margin: 0;
    width: 1200px;
    height: 800px;
    overflow: hidden;
    background: var(--page-bg);
  }
  .cover-wrap {
    position: absolute;
    left: 183px;
    top: 100px;
    width: 834px;
    height: 600px;
    display: flex;
    background: var(--paper);
    box-shadow: 0 10px 30px rgba(0,0,0,0.22);
  }
  .back-cover, .front-cover {
    position: relative;
    width: 400px;
    height: 600px;
    overflow: hidden;
    background: var(--paper);
  }
  .spine {
    width: 34px;
    height: 600px;
    background: var(--paper);
    border-left: 1px solid var(--edge);
    border-right: 1px solid var(--edge);
    box-sizing: border-box;
    display: flex;
    align-items: center;
    justify-content: center;
  }
  .spine-text {
    writing-mode: vertical-rl;
    font-family: "Montserrat", sans-serif;
    font-weight: 800;
    font-size: 13px;
    letter-spacing: 2.5px;
    color: var(--ink);
    white-space: nowrap;
  }
  .spine-accent { color: var(--gold); }
  .spine-dash { margin: 10px 0; }

  .cover-scene {
    position: absolute;
    left: 0;
    right: 0;
    bottom: 0;
    height: 62%;
    background:
      radial-gradient(ellipse 55% 16% at 50% 20%, var(--glow) 0%, rgba(255,210,120,0.55) 45%, rgba(237,162,74,0) 100%),
      linear-gradient(180deg, var(--paper) 0%, var(--dusk) 12%, var(--sunset) 18%, var(--glow) 22%, var(--field) 34%, var(--road) 62%, var(--road-deep) 100%);
  }
  .back-cover .cover-scene {
    height: 30%;
    background: linear-gradient(180deg, var(--paper) 0%, #e6d7c4 25%, #a88a66 60%, #5a4a44 100%);
  }

  .front-text, .back-text {
    position: absolute;
    left: 0;
    right: 0;
    text-align: center;
    color: var(--ink);
    font-family: "Montserrat", sans-serif;
  }
  .front-text { top: 40px; }
  .author-name {
    font-weight: 700;
    font-size: 12px;
    letter-spacing: 3px;
    margin: 0 0 28px;
  }
  .title { margin: 0; font-weight: 800; line-height: 1; }
  .title-lead { display: block; font-size: 24px; letter-spacing: 1.5px; }
  .title-key { display: block; font-size: 66px; letter-spacing: 3px; color: var(--gold); margin-top: 4px; }
  .title-end { display: block; font-size: 42px; letter-spacing: 3px; margin-top: 2px; }
  .subtitle {
    margin: 12px 0 0;
    font-weight: 700;
    font-size: 11px;
    letter-spacing: 1px;
    color: var(--gold);
  }

  .back-text { top: 40px; padding: 0 28px; }
  .back-text .title-lead { font-size: 17px; }
  .back-text .title-key { font-size: 46px; }
  .back-text .title-end { font-size: 29px; }
  .back-text .subtitle { font-size: 8px; margin-top: 8px; }
  .blurb, .bio, .fine-print {
    font-family: "Open Sans", sans-serif;
    color: var(--ink-body);
    text-align: justify;
  }
  .blurb { font-size: 10.5px; line-height: 1.55; margin: 18px 0 0; }
  .author-block {
    display: flex;
    gap: 12px;
    align-items: flex-start;
    margin-top: 18px;
  }
  .author-portrait {
    flex: none;
    width: 64px;
    height: 78px;
    background: linear-gradient(180deg, #d4d6da, var(--portrait));
  }
  .bio { font-size: 10px; line-height: 1.55; margin: 0; }
  .fine-print { font-size: 7.5px; line-height: 1.5; margin: 14px 0 0; }
</style>
</head>
<body>
  <div class="cover-wrap">
    <section class="back-cover">
      <div class="cover-scene" role="img" aria-label="Soft evening field photograph fading into the white page"></div>
      <div class="back-text">
        <h2 class="title">
          <span class="title-lead">WALKING BESIDE THE</span>
          <span class="title-key">QUIET</span>
          <span class="title-end">RIVER</span>
        </h2>
        <p class="subtitle">A STUDY OF REFUGE, PURPOSE &amp; CALLING</p>
        <p class="blurb">This gentle study invites every reader to slow down and walk with a Father who is near. Through honest reflection, scripture and quiet practice, you will discover refuge in seasons of fear, purpose in seasons of doubt and a calling that grows from simple trust. Each chapter opens the heart to a God who is present, gracious and kind.</p>
        <div class="author-block">
          <div class="author-portrait" role="img" aria-label="Author portrait photograph"></div>
          <p class="bio">Tom Pettigrew has taught small groups for many years, helping people find rest in God and walk forward with fresh hope and purpose.</p>
        </div>
        <p class="fine-print">He lives near the river with his family, where he writes, walks each morning and meets with friends who are learning to listen for the quiet voice of the Father in ordinary days.</p>
      </div>
    </section>

    <div class="spine">
      <span class="spine-text">WALKING BESIDE THE <span class="spine-accent">QUIET</span> RIVER<span class="spine-dash">—</span>TOM PETTIGREW</span>
    </div>

    <section class="front-cover">
      <div class="cover-scene" role="img" aria-label="Sunset photograph of a long straight road with a cross painted on it, leading toward a glowing horizon and fading into the white page"></div>
      <div class="front-text">
        <p class="author-name">TOM PETTIGREW</p>
        <h1 class="title">
          <span class="title-lead">WALKING BESIDE THE</span>
          <span class="title-key">QUIET</span>
          <span class="title-end">RIVER</span>
        </h1>
        <p class="subtitle">A STUDY OF REFUGE, PURPOSE &amp; CALLING</p>
      </div>
    </section>
  </div>
</body>
</html>
```